Minimalist Sign Design (24” X 24”)

I am wanting to redesign our yard signs to be very clean, attractive, eye catching, and readable (imagine driving by a home with a sign In yard). We paint homes. I am hoping to have a design that incorporates our brand colors in a clean, professional way that represents our company. Clean, concise, easily read from a distance.

Target Market(s)

Homeowners

Industry/Entity Type

Painting And Decorating

Font styles to use
Sans Serif

Requirements
Must have
• Phone Number: (739) 418-5067
• Free Consultations
• Makeover in progress!
• Brand colors:
• Hunter Green: #355e3b
• Black
• White
Nice to have
• Would like the hunter green to he background color of sign. Can make logo white to stand out with the green.
Should not have
• Too busy or unable to read text

```html
<!DOCTYPE html>
<html lang="en">
<head>
<meta charset="utf-8">
<title>Birchline Painting Yard Sign</title>
<link rel="stylesheet" href="https://fonts.googleapis.com/css2?family=Montserrat:wght@500;600;700&display=swap">
<style>
  :root {
    --hunter-green: #355e3b;
    --ink: #000000;
    --paper: #ffffff;
    --backdrop: #231f20;
  }
  html, body {
    margin: 0;
    padding: 0;
    width: 1200px;
    height: 1200px;
    overflow: hidden;
    background: var(--backdrop);
    font-family: "Montserrat", Arial, sans-serif;
  }
  .sign {
    position: absolute;
    left: 141px;
    top: 141px;
    width: 918px;
    height: 918px;
    background: var(--paper);
    overflow: hidden;
  }
  .sign__headline {
    position: absolute;
    top: 30px;
    left: 0;
    width: 100%;
    margin: 0;
    text-align: center;
    color: var(--hunter-green);
    font-weight: 700;
    font-size: 63px;
    letter-spacing: -0.5px;
    line-height: 1;
  }
  .sign__brand {
    position: absolute;
    top: 126px;
    left: 0;
    width: 100%;
    height: 506px;
    display: flex;
    flex-direction: column;
    align-items: center;
    justify-content: center;
    color: var(--ink);
    font-weight: 600;
    font-size: 124px;
    letter-spacing: 8px;
    line-height: 1.15;
    text-align: center;
  }
  .sign__brand-line {
    display: block;
    padding-left: 8px;
    white-space: nowrap;
  }
  .sign__divider {
    position: absolute;
    left: 0;
    top: 688px;
    width: 918px;
    height: 26px;
  }
  .sign__contact {
    position: absolute;
    left: 0;
    top: 697px;
    width: 100%;
    height: 221px;
    background: var(--hunter-green);
    color: var(--paper);
    text-align: center;
  }
  .sign__phone {
    position: absolute;
    top: 28px;
    left: 0;
    width: 100%;
    margin: 0;
    font-weight: 500;
    font-size: 99px;
    letter-spacing: 1px;
    line-height: 1;
  }
  .sign__offer {
    position: absolute;
    top: 136px;
    left: 0;
    width: 100%;
    margin: 0;
    font-weight: 500;
    font-size: 64px;
    line-height: 1;
  }
</style>
</head>
<body>
  <main class="sign">
    <h1 class="sign__headline">MAKEOVER IN PROGRESS!</h1>

    <div class="sign__brand">
      <span class="sign__brand-line">BIRCHLINE</span>
      <span class="sign__brand-line">PAINTING</span>
    </div>

    <section class="sign__contact">
      <p class="sign__phone">(739) 418-5067</p>
      <p class="sign__offer">FREE CONSULTATION</p>
    </section>

    <svg class="sign__divider" viewBox="0 0 918 26" aria-hidden="true">
      <rect x="0" y="0" width="918" height="10" fill="var(--ink)"/>
      <polygon points="428,0 490,0 459,22" fill="var(--paper)"/>
    </svg>
  </main>
</body>
</html>
```